Flyer-Design für ambulanten Pflegedienst
Zielgruppe
Wir sind ein ambulanter Pflegedienst in Rostock und in Gnoien. Patienten werden in der Häuslichkeit versorgt.
Aufgabenstellung
Folgender Flyer soll erstellt werden.
Das Format kann vom Designer festgelegt werden:
Ein paar Flyer habe ich mit hochgeladen. Es sollte jedoch einmal ein ganz neues modernes Design sein.
Vorderseite:Text:
Sie kommen mit den alltäglichen Dingen des Lebens
nicht mehr gut alleine zurecht?
Wir unterstützen Sie gerne bei der Beantragung eines
Pflegegrades. Nachdem der Gesundheitliche Prüfstelle der Versicherer
sich angemeldet hat, begleiten wir Sie bei der Begutachtung.
Rückseite:
Pflegeberatung:
Wenn Sie einen Pflegegrad haben und von einer privaten Pflegeperson
versorgt werden, erwartet Ihre Pflegekasse in regelmäßigen Abständen einen Beratungebesuch
von einem anerkannten Pflegedienst.
Bitte beide Logos vom Pflegezentrum Lindenhof und vom Pflegedienst Karunel auf den Flyer
Auch beide Adressen auf den Flyer:

```html
<!DOCTYPE html>
<html lang="de">
<head>
<meta charset="utf-8">
<title>Flyer Pflegeberatung</title>
<link rel="stylesheet" href="https://fonts.googleapis.com/css2?family=Fira+Sans:ital,wght@0,400;0,600;0,700;1,300;1,400&display=swap">
<style>
  :root{
    --stage:#8c8c8c;
    --navy:#1f2b5c;
    --ink:#1a1a1a;
    --green-strong:#8fc66c;
    --green-soft:#c6dd86;
    --green-pale:#e7efd2;
    --white:#ffffff;
    --photo-warm-a:#d8c2aa;
    --photo-warm-b:#efe6dc;
    --photo-cool-a:#e9e6e2;
    --photo-cool-b:#b9b3ad;
  }
  *{box-sizing:border-box;margin:0;padding:0}
  html,body{width:1200px;height:518px;overflow:hidden}
  body{background:var(--stage);font-family:"Fira Sans",sans-serif;position:relative}
  .flyer{position:absolute;top:84px;width:456px;height:322px;background:var(--white);overflow:hidden}
  .flyer--back{left:110px}
  .flyer--front{left:635px}
  .flyer__shapes{position:absolute;inset:0;width:456px;height:322px}
  .text{position:absolute;color:var(--navy);white-space:nowrap}

  /* back side */
  .advice__title{left:22px;top:52px;font-size:10.5px;font-weight:700}
  .advice__body{left:22px;top:79px;font-size:7.3px;line-height:10.1px;font-weight:400}
  .advice__call{left:22px;top:131px;font-size:9.4px;line-height:13px;font-style:italic;font-weight:300}
  .advice__call strong{font-style:normal;font-weight:700}
  .partner{position:absolute;right:0;background:var(--white);border-radius:10px 0 0 10px;box-shadow:0 2px 6px rgba(0,0,0,.18);color:var(--ink);font-size:6.8px;line-height:9.2px;font-style:normal;white-space:nowrap}
  .partner--lindenhof{left:317px;top:34px;height:139px;padding:14px 0 0 12px}
  .partner--karunel{left:268px;top:182px;height:100px;padding:12px 0 0 12px}
  .partner__mark{display:flex;align-items:center;gap:5px;height:62px;font-size:9.5px;font-weight:600;color:var(--navy)}
  .partner--karunel .partner__mark{height:44px}
  .partner__dot{width:14px;height:14px;border-radius:50%;background:var(--green-strong);flex:none}
  .partner__name{font-size:8px;font-weight:700;line-height:11px;margin-bottom:1px}

  /* front side */
  .headline{position:absolute;left:0;top:25px;width:323px;height:50px;background:var(--white);border-radius:0 10px 10px 0;box-shadow:0 2px 6px rgba(0,0,0,.18);padding:9px 0 0 21px;color:var(--navy);font-size:11.8px;font-weight:700;line-height:17.5px;letter-spacing:-0.15px;white-space:nowrap}
  .support__title{left:22px;top:102px;font-size:9.6px;font-weight:700;line-height:13px}
  .support__body{left:22px;top:142px;font-size:7.3px;line-height:10px}
  .contact-oval{position:absolute;left:34px;top:195px;width:164px;height:114px;border-radius:50%;background:var(--white);box-shadow:0 2px 6px rgba(0,0,0,.18);text-align:center;color:var(--navy);padding-top:30px;white-space:nowrap}
  .contact-oval__lead{font-size:9px;line-height:13px;font-style:italic;font-weight:300}
  .contact-oval__phone{font-size:12.5px;font-weight:700;margin-top:3px}
</style>
</head>
<body>

<section class="flyer flyer--back">
  <svg class="flyer__shapes" viewBox="0 0 456 322">
    <defs>
      <linearGradient id="bandBack" x1="0" x2="1">
        <stop offset="0" stop-color="var(--green-strong)"/><stop offset="1" stop-color="var(--green-soft)"/>
      </linearGradient>
      <linearGradient id="photoBack" x1="0" y1="0" x2="1" y2="1">
        <stop offset="0" stop-color="var(--photo-warm-a)"/><stop offset="1" stop-color="var(--photo-warm-b)"/>
      </linearGradient>
    </defs>
    <polygon points="0,0 325,0 318,25 0,25" fill="url(#bandBack)"/>
    <polygon points="0,25 318,25 255,203 0,203" fill="var(--green-pale)"/>
    <g role="img" aria-label="Foto: ältere Dame im Rollstuhl, eine Pflegerin legt ihr die Hände auf die Schultern">
      <polygon points="0,203 255,203 212,322 0,322" fill="url(#photoBack)"/>
    </g>
  </svg>

  <h2 class="text advice__title">Pflegeberatung</h2>
  <p class="text advice__body">Wenn Sie einen Pflegegrad haben und von einer privaten<br>Pflegeperson versorgt werden, erwartet Ihre Pflegekasse in<br>regelmäßigen Abständen einen Beratungebesuch von einem<br>anerkannten Pflegedienst.</p>
  <p class="text advice__call">Vereinbaren Sie unter der Telefonnummer<br><strong>0800 44 44 712</strong> rechtzeitig einen Termin, damit<br>Ihre optimale Versorgung weiterhin sichergestellt ist.</p>

  <address class="partner partner--lindenhof">
    <div class="partner__mark"><span class="partner__dot"></span>Pflegezentrum Lindenhof</div>
    <div class="partner__name">Pflegezentrum Lindenhof GmbH</div>
    Lindenweg 12<br>18057 Rostock<br>Tel. 0800 4444712<br>www.pflegezentrum-lindenhof.de
  </address>

  <address class="partner partner--karunel">
    <div class="partner__mark"><span class="partner__dot"></span>Karunel</div>
    <div class="partner__name">Karunel Der mobile Pflegedienst GmbH</div>
    Am Markt 21<br>17179 Gnoien<br>www.karunel.de
  </address>
</section>

<section class="flyer flyer--front">
  <svg class="flyer__shapes" viewBox="0 0 456 322">
    <defs>
      <linearGradient id="bandFront" x1="0" x2="1">
        <stop offset="0" stop-color="var(--green-strong)"/><stop offset="1" stop-color="var(--green-soft)"/>
      </linearGradient>
      <linearGradient id="photoFront" x1="0" y1="0" x2="1" y2="1">
        <stop offset="0" stop-color="var(--photo-cool-a)"/><stop offset="1" stop-color="var(--photo-cool-b)"/>
      </linearGradient>
    </defs>
    <rect width="456" height="322" fill="var(--green-pale)"/>
    <polygon points="0,0 265,0 256,25 0,25" fill="url(#bandFront)"/>
    <polygon points="0,286 164,286 152,322 0,322" fill="url(#bandFront)"/>
    <g role="img" aria-label="Foto: Pflegerin hilft einer lächelnden älteren Frau beim Zuknöpfen der Bluse">
      <polygon points="265,0 456,0 456,322 152,322" fill="url(#photoFront)"/>
    </g>
  </svg>

  <h1 class="headline">Sie kommen mit den alltäglichen<br>Dingen des Lebens nicht mehr gut alleine zurecht?</h1>
  <h2 class="text support__title">Wir unterstützen Sie gerne bei<br>der Beantragung eines Pflegegrades.</h2>
  <p class="text support__body">Nachdem der Gesundheitliche Prüfstelle<br>der Versicherer sich angemeldet hat,<br>begleiten wir Sie bei der Begutachtung.</p>

  <div class="contact-oval">
    <p class="contact-oval__lead">Unsere freundlichen Mitarbeiter<br>erreichen Sie unter der<br>Telefonnummer:</p>
    <p class="contact-oval__phone">0800 44 44 712</p>
  </div>
</section>

</body>
</html>
```